Medical Company in need of Modern business card design for new Wound Care clinic.

Modern business card design for our Woundcare company. Logo and description of services can be found on our website; https://www.tovrel-woundcare.com/

```html
<!DOCTYPE html>
<html lang="en">
<head>
<meta charset="utf-8">
<title>Tovrel Woundcare – Business Card</title>
<link rel="stylesheet" href="https://fonts.googleapis.com/css2?family=Montserrat:wght@500&family=Open+Sans:wght@400;700&display=swap">
<style>
  :root {
    --canvas: #e9e6e1;
    --card-dark: #2b2a2d;
    --card-dark-band: #222124;
    --card-light: #ffffff;
    --gold: #c8962e;
    --gold-deep: #a9791f;
    --ink: #3a3a3c;
  }
  * { margin: 0; padding: 0; box-sizing: border-box; }
  html, body { width: 1200px; height: 900px; overflow: hidden; }
  body {
    background: var(--canvas);
    display: flex; flex-direction: column; align-items: center; justify-content: center;
    gap: 30px;
  }
  .card {
    position: relative;
    width: 700px; height: 400px;
    border-radius: 34px;
    overflow: hidden;
    box-shadow: 0 14px 30px rgba(0,0,0,.18);
  }
  .card--back { background: var(--card-dark); }
  .card--front { background: var(--card-light); }
  .card__band {
    position: absolute; left: 0; right: 0; bottom: 0; height: 46px;
    background: var(--card-dark-band);
    border-top: 4px solid var(--gold);
  }
  .card--front .card__band { background: var(--card-dark); }
  .wordmark {
    position: absolute; left: 0; right: 0; top: 150px;
    display: flex; align-items: center; justify-content: center; gap: 18px;
    font-family: "Montserrat", sans-serif; font-weight: 500;
    font-size: 38px; letter-spacing: 9px; text-transform: uppercase;
    color: var(--gold);
  }
  .card--front .wordmark { top: 95px; }
  .wordmark__square { width: 22px; height: 22px; background: var(--gold); }
  .contact {
    position: absolute; left: 60px; bottom: 82px;
    display: flex; flex-direction: column; gap: 12px;
    font-family: "Open Sans", sans-serif; color: var(--ink);
  }
  .contact__name { font-size: 22px; }
  .contact__name strong { color: var(--gold); font-weight: 700; letter-spacing: .5px; }
  .contact__name span { color: var(--gold); margin: 0 8px; }
  .contact__rows { display: flex; align-items: stretch; gap: 18px; }
  .contact__col { display: flex; flex-direction: column; gap: 6px; font-size: 18px; }
  .contact__divider { width: 1.5px; background: var(--ink); }
  .contact__item { display: flex; align-items: center; gap: 8px; }
  .contact__item svg { width: 18px; height: 18px; flex: none; }
</style>
</head>
<body>
  <section class="card card--back">
    <div class="wordmark"><span class="wordmark__square"></span>Tovrel Woundcare</div>
    <div class="card__band"></div>
  </section>

  <section class="card card--front">
    <div class="wordmark"><span class="wordmark__square"></span>Tovrel Woundcare</div>
    <div class="contact">
      <p class="contact__name"><strong>DANIEL MERCER</strong><span>|</span>Director</p>
      <div class="contact__rows">
        <div class="contact__col">
          <p class="contact__item">
            <svg viewBox="0 0 24 24" fill="var(--gold)"><path d="M6.6 10.8a15 15 0 0 0 6.6 6.6l2.2-2.2c.3-.3.7-.4 1-.2 1.1.4 2.3.6 3.6.6.6 0 1 .4 1 1V20c0 .6-.4 1-1 1A17 17 0 0 1 3 4c0-.6.4-1 1-1h3.5c.6 0 1 .4 1 1 0 1.3.2 2.5.6 3.6.1.3 0 .7-.2 1z"/></svg>
            972-555-0148
          </p>
          <p class="contact__item">
            <svg viewBox="0 0 24 24" fill="var(--gold)"><path d="M7 3h10v5H7zM4 9h16a2 2 0 0 1 2 2v6h-4v4H6v-4H2v-6a2 2 0 0 1 2-2zm4 7v3h8v-3z"/></svg>
            972-555-0149
          </p>
        </div>
        <div class="contact__divider"></div>
        <div class="contact__col">
          <p class="contact__item">
            <svg viewBox="0 0 24 24" fill="none" stroke="var(--gold)" stroke-width="1.8"><circle cx="12" cy="12" r="9"/><path d="M3 12h18M12 3c3 3.5 3 14.5 0 18M12 3c-3 3.5-3 14.5 0 18"/></svg>
            www.tovrel-woundcare.com
          </p>
          <p class="contact__item">
            <svg viewBox="0 0 24 24" fill="var(--gold)"><path d="M12 2a7 7 0 0 0-7 7c0 5 7 13 7 13s7-8 7-13a7 7 0 0 0-7-7zm0 9.5A2.5 2.5 0 1 1 12 6.5a2.5 2.5 0 0 1 0 5z"/></svg>
            4120 Birchwood Lane Bldg. C, suite 118
          </p>
        </div>
      </div>
    </div>
    <div class="card__band"></div>
  </section>
</body>
</html>
```